Business Card Design for Cybersecurity Company - Quorvent Systems

We need a business card design for our new cybersecurity company, Quorvent. We’re going for a clean, hi tech look that feels modern, premium, and trustworthy. We want a design that really stands out and makes people say WOW when we hand it over!

Quorvent delivers reliable IT support and managed services for small and mid sized businesses. We help companies stay secure, efficient, and connected through proactive monitoring, cybersecurity services, cloud management, and remote support.

Target Market(s)

Designers should target small and mid sized businesses that need dependable cybersecurity and IT support.

Industry/Entity Type

Cybersecurity, Managed Service Provider, IT services

Contact Information for Business Card

Contact information

Requirements
Must have
• The card should look clean, modern, and tech focused, with the Quorvent logo, clear contact info, and strong readability. It needs to feel premium and professional while still keeping a simple layout that fits a cybersecurity and IT brand.
Nice to have
• Nice to have elements include subtle touches that give the card a modern, tech feel, along with a layout that works well in different background styles.
Should not have
• The card should avoid clutter, loud graphics, or anything that takes attention away from the logo and contact details.

```html
<!DOCTYPE html>
<html lang="en">
<head>
<meta charset="utf-8">
<title>Quorvent Systems — Business Card</title>
<link href="https://fonts.googleapis.com/css2?family=Arimo:wght@400;700&display=swap" rel="stylesheet">
<style>
  :root {
    --backdrop: #e9e6e1;
    --front-blue: #3b78b4;
    --front-violet: #6c48a8;
    --back-navy: #0d1120;
    --ink-white: #ffffff;
    --ink-soft: #d9dcea;
    --accent-blue: #4a7fd0;
    --accent-violet: #7a55c4;
    --rule-violet: #6d4fb8;
  }
  html, body {
    margin: 0;
    padding: 0;
    width: 1200px;
    height: 900px;
    overflow: hidden;
    background: var(--backdrop);
    font-family: "Arimo", Arial, sans-serif;
  }
  .stage {
    position: relative;
    width: 1200px;
    height: 900px;
  }
  .card {
    position: absolute;
    width: 600px;
    height: 343px;
    border-radius: 26px;
    overflow: hidden;
    box-shadow: 0 14px 30px rgba(0,0,0,0.22);
  }
  /* Front face */
  .card-front {
    left: 100px;
    top: 80px;
    background: linear-gradient(200deg, var(--front-violet) 0%, #5358ac 45%, var(--front-blue) 100%);
  }
  .front-brand {
    position: absolute;
    right: 48px;
    top: 48px;
    text-align: left;
    color: var(--ink-white);
  }
  .brand-name {
    font-weight: 700;
    font-size: 52px;
    letter-spacing: 1px;
    line-height: 1;
  }
  .brand-tagline {
    font-weight: 400;
    font-size: 18px;
    letter-spacing: 12px;
    margin-top: 6px;
    color: var(--ink-soft);
  }
  .front-web {
    margin-top: 18px;
    font-size: 15px;
    letter-spacing: 1px;
    text-align: center;
    color: var(--ink-white);
  }
  /* Back face */
  .card-back {
    left: 500px;
    top: 470px;
    background: var(--back-navy);
  }
  .contact-block {
    position: absolute;
    left: 40px;
    top: 52px;
    width: 300px;
  }
  .person-name {
    font-weight: 700;
    font-size: 24px;
    letter-spacing: 0.5px;
    background: linear-gradient(90deg, var(--accent-blue), var(--accent-violet));
    -webkit-background-clip: text;
    background-clip: text;
    color: transparent;
    margin: 0;
  }
  .person-role,
  .person-company {
    font-size: 18px;
    color: var(--ink-white);
    margin: 4px 0 0 14px;
  }
  .divider {
    height: 2px;
    width: 250px;
    margin: 16px 0 18px 28px;
    background: linear-gradient(90deg, var(--accent-violet), var(--rule-violet) 70%, transparent);
  }
  .contact-list {
    list-style: none;
    margin: 0;
    padding: 0 0 0 34px;
  }
  .contact-list li {
    display: flex;
    align-items: center;
    gap: 10px;
    font-size: 18px;
    color: var(--ink-white);
    margin-bottom: 8px;
  }
  .contact-icon {
    width: 16px;
    height: 16px;
    flex: none;
  }
  .back-brand {
    position: absolute;
    right: 40px;
    top: 150px;
    display: flex;
    align-items: center;
    gap: 16px;
    color: var(--ink-white);
  }
  .brand-dot {
    width: 62px;
    height: 62px;
    border-radius: 50%;
    border: 3px solid var(--accent-blue);
    box-sizing: border-box;
  }
  .back-brand .brand-name { font-size: 40px; }
  .back-brand .brand-tagline { font-size: 14px; letter-spacing: 9px; }
</style>
</head>
<body>
<main class="stage">

  <section class="card card-front" aria-label="Card front">
    <div class="front-brand">
      <div class="brand-name">Quorvent</div>
      <div class="brand-tagline">Systems</div>
      <div class="front-web">www.quorvent.com</div>
    </div>
  </section>

  <section class="card card-back" aria-label="Card back">
    <div class="contact-block">
      <h1 class="person-name">DORIAN HALE</h1>
      <p class="person-role">Owner | CEO</p>
      <p class="person-company">Quorvent Systems</p>
      <div class="divider"></div>
      <ul class="contact-list">
        <li>
          <svg class="contact-icon" viewBox="0 0 16 16" aria-hidden="true">
            <rect x="4" y="1" width="8" height="14" rx="1.5" fill="none" stroke="#4a7fd0" stroke-width="1.5"/>
            <circle cx="8" cy="12.5" r="0.9" fill="#4a7fd0"/>
          </svg>
          (555) 304-7182
        </li>
        <li>
          <svg class="contact-icon" viewBox="0 0 16 16" aria-hidden="true">
            <path d="M3 2l3 0 1 3.5-1.8 1.2a8 8 0 0 0 4.1 4.1L10.5 9 14 10v3a1 1 0 0 1-1 1A11 11 0 0 1 2 3a1 1 0 0 1 1-1z" fill="#4a7fd0"/>
          </svg>
          (555) 210-QUOR
        </li>
        <li>
          <svg class="contact-icon" viewBox="0 0 16 16" aria-hidden="true">
            <rect x="1" y="3.5" width="14" height="9" rx="1" fill="#4a7fd0"/>
            <path d="M1.5 4l6.5 5 6.5-5" fill="none" stroke="#0d1120" stroke-width="1.2"/>
          </svg>
          dorian@quorvent.com
        </li>
        <li>
          <svg class="contact-icon" viewBox="0 0 16 16" aria-hidden="true">
            <g fill="none" stroke="#4a7fd0" stroke-width="1.2">
              <circle cx="8" cy="8" r="6.5"/>
              <ellipse cx="8" cy="8" rx="3" ry="6.5"/>
              <path d="M1.5 8h13M2.5 4.8h11M2.5 11.2h11"/>
            </g>
          </svg>
          www.quorvent.com
        </li>
      </ul>
    </div>

    <div class="back-brand">
      <span class="brand-dot" aria-hidden="true"></span>
      <div>
        <div class="brand-name">Quorvent</div>
        <div class="brand-tagline">Systems</div>
      </div>
    </div>
  </section>

</main>
</body>
</html>
```